Healthcare website - Diabetic Shoes - Elderfund - No Cost

I am looking to upgrade my website. I do not want to use Wordpress, Adobe Muse or another designing program. The code should be easily editable using textpad or VI. After the project is done I want to easily add my custom PHP code.

Features
Creative and Modern Design .
Fully responsive site for use on mobile devices
bootstrap, jquery

My current website is
www.pebblewalkco.com

Target Market(s)

Older people who have diabetes. Target market is +60 years old, but we do have younger people going to the site to help out their parents.

Industry/Entity Type

Healthcare

Coding

Coded - Design and coding required

Number of Pages Required

2 page

Colors

Designer to choose colors to be used in the design.

Requirements
Must have
• The code should be easily editable using textpad or VI. After the project is done I want to easily add my custom PHP code.
• The first page will be the home page and the other page I need is this form.
• https://www.pebblewalkco.com/pebble-walk-co-do-i-qualify.php
Should not have
• I do not want to use Wordpress, Adobe Muse or another designing program.

```html
<!DOCTYPE html>
<html lang="en">
<head>
<meta charset="utf-8">
<title>Pebble Walk Co – Diabetic Shoes Covered by Elderfund</title>
<link href="https://fonts.googleapis.com/css2?family=Open+Sans:wght@400;600;700;800&display=swap" rel="stylesheet">
<style>
:root{
  --brand-blue:#4b7aa5;
  --brand-blue-dark:#3c6790;
  --link-blue:#2f72b5;
  --ink:#333638;
  --ink-soft:#555a5e;
  --line:#c9cdd1;
  --highlight:#f3d63b;
  --footer:#1f2226;
  --footer-text:#d6d9dc;
  --white:#ffffff;
}
*{box-sizing:border-box;margin:0;padding:0}
html,body{width:1200px;height:3542px;overflow:hidden}
body{font-family:"Open Sans",Arial,sans-serif;color:var(--ink);background:var(--white);position:relative}
.abs{position:absolute}

/* top bar + nav */
.topbar{left:0;top:0;width:1200px;height:32px;background:var(--brand-blue)}
.topbar .contact{right:70px;top:8px;font-size:11px;color:var(--white);display:flex;gap:14px;align-items:center}
.topbar .dot{width:16px;height:16px;border:1px solid var(--white);border-radius:50%;display:inline-block}
.site-header{left:0;top:32px;width:1200px;height:106px;background:var(--white)}
.logo{display:flex;align-items:center;gap:8px;font-size:30px;font-weight:600;color:var(--brand-blue);letter-spacing:.5px}
.logo .mark{width:14px;height:14px;border-radius:50%;background:var(--brand-blue)}
.site-header .logo{left:60px;top:32px}
.main-nav{right:30px;top:45px;display:flex;gap:24px;font-size:12px;color:var(--ink-soft);text-transform:uppercase}

/* hero */
.hero{left:0;top:138px;width:1200px;height:472px;background:linear-gradient(180deg,#7a5a3e 0%,#5e4230 45%,#8b6a4b 100%)}
.hero-title{left:0;top:24px;width:1200px;text-align:center;font-weight:800;font-size:38px;line-height:46px;color:var(--white)}
.hero-title span{color:var(--highlight);display:block}
.hero-text{left:240px;top:124px;width:720px;text-align:center;font-size:15px;line-height:20px;color:var(--white)}
.hero-shoes{left:90px;top:230px;width:1020px;height:200px;border-radius:8px;background:linear-gradient(90deg,rgba(120,70,50,.35),rgba(90,90,95,.35),rgba(150,110,80,.35),rgba(120,90,170,.35))}
.hero-arrow{top:214px;width:36px;height:36px}
.hero-dots{left:0;top:436px;width:1200px;display:flex;justify-content:center;gap:14px}
.hero-dots i{width:18px;height:18px;border-radius:50%;background:rgba(255,255,255,.55)}
.hero-dots i:first-child{background:var(--white)}

/* steps */
.steps{left:0;top:610px;width:1200px;height:347px;background:var(--brand-blue);color:var(--white)}
.steps h2{position:absolute;top:28px;width:100%;text-align:center;font-size:29px;font-weight:700}
.steps .rule{position:absolute;left:560px;top:82px;width:80px;height:2px;background:var(--white)}
.step{position:absolute;top:110px;width:220px;text-align:center;font-size:15px;line-height:20px}
.step svg{display:block;margin:0 auto 16px}

/* catalog form */
.catalog{left:0;top:957px;width:1200px;height:561px}
.catalog h2{position:absolute;top:30px;width:100%;text-align:center;font-size:31px;font-weight:600;color:var(--ink)}
.catalog .rule{position:absolute;left:560px;top:86px;width:80px;height:2px;background:var(--ink)}
.field{position:absolute;width:316px}
.field label{display:block;font-size:12px;font-weight:700;margin-bottom:6px}
.field .box{height:30px;border:1px solid #9aa0a6;border-radius:3px;font-size:11px;color:#777;padding:7px 8px}
.field .box.tall{height:78px}
.btn{display:inline-block;background:var(--brand-blue);color:var(--white);font-size:18px;text-align:center;border-radius:3px}
.catalog .btn{position:absolute;left:504px;top:490px;width:193px;height:36px;line-height:36px}

/* info band */
.info{left:0;top:1518px;width:1200px;height:285px;background:var(--brand-blue);color:var(--white)}
.info-col{position:absolute;top:42px;width:280px;text-align:center}
.info-col h3{font-size:11px;font-weight:700;margin-bottom:12px}
.info-col p{font-size:9.5px;line-height:13px;margin-bottom:10px}

/* about */
.about h2{font-size:31px;font-weight:700;letter-spacing:.5px}
.about p{font-size:15.5px;line-height:23px;color:var(--ink-soft)}
.photo-block{background:linear-gradient(160deg,#cfe0ef,#a7b8c6 55%,#5f7e52)}
.divider{left:60px;width:1080px;height:1px;background:var(--line)}
.philosophy h2,.manufacturers h2{width:1200px;text-align:center;font-size:31px;font-weight:700}
.philosophy p{left:180px;width:840px;text-align:center;font-size:15px;line-height:19px;color:var(--ink-soft)}
.partner{height:80px;border-radius:50%}

/* catalog links */
.cta-line{left:0;width:1200px;text-align:center;font-size:20px;font-weight:700;color:var(--ink)}
.cta-line .link{color:var(--link-blue)}
.frame{border:5px solid var(--brand-blue);background:var(--white)}
.frame .fill{position:absolute;inset:8px}

/* footer */
.site-footer{left:0;top:3258px;width:1200px;height:284px;background:var(--footer);color:var(--footer-text)}
.site-footer .logo{color:#e6e8ea;font-size:34px}
.footer-nav{left:511px;top:60px;font-size:13px;line-height:20px;text-transform:uppercase}
.footer-cta{left:868px;top:60px;width:220px;font-size:17px;font-weight:700;line-height:20px;color:var(--white)}
.social{width:30px;height:30px;border:2px solid var(--footer-text);border-radius:50%}
.copyright{left:0;top:260px;width:1200px;text-align:center;font-size:9px;color:#7c8186}
</style>
</head>
<body>

<div class="abs topbar">
  <div class="abs contact"><span>1-800-555-0142 · Call Us</span><span class="dot"></span><span class="dot"></span><span>LOGIN</span></div>
</div>

<header class="abs site-header">
  <div class="abs logo"><span class="mark"></span>Pebble Walk Co</div>
  <nav class="abs main-nav">
    <span>Home</span><span>Pebble Walk Co Do I Qualify?</span><span>Why Diabetic Shoes?</span><span>Shoes</span><span>Products</span><span>Shoe Fitter Jobs</span><span>FAQ</span>
  </nav>
</header>

<section class="abs hero">
  <div class="abs hero-shoes" role="img" aria-label="Photo of four diabetic shoes and sneakers on a wooden floor"></div>
  <h1 class="abs hero-title">DIABETIC SHOES OR SNEAKERS <span>COVERED BY ELDERFUND</span></h1>
  <p class="abs hero-text">No or little out of pocket Cost To You!* Elderfund, and most insurance plans, may cover the cost of one pair of diabetic shoes and three pairs of custom inserts per calendar year. Co-payments, deductibles and some restrictions apply.</p>
  <svg class="abs hero-arrow" style="left:6px" viewBox="0 0 36 36"><circle cx="18" cy="18" r="16" fill="none" stroke="#fff" stroke-width="2"/><path d="M21 11l-7 7 7 7" fill="none" stroke="#fff" stroke-width="2.5"/></svg>
  <svg class="abs hero-arrow" style="right:6px" viewBox="0 0 36 36"><circle cx="18" cy="18" r="16" fill="none" stroke="#fff" stroke-width="2"/><path d="M15 11l7 7-7 7" fill="none" stroke="#fff" stroke-width="2.5"/></svg>
  <div class="abs hero-dots"><i></i><i></i><i></i><i></i><i></i><i></i><i></i></div>
</section>

<section class="abs steps">
  <h2>4 Easy Steps To Receive Your New Therapeutic Shoes.</h2>
  <div class="rule"></div>
  <div class="step" style="left:110px">
    <svg width="110" height="110" viewBox="0 0 110 110"><circle cx="55" cy="55" r="52" fill="none" stroke="#fff" stroke-width="3"/><path d="M40 30h22l10 10v40H40z" fill="none" stroke="#fff" stroke-width="3"/><path d="M47 50h18M47 59h18M47 68h18" stroke="#fff" stroke-width="3"/></svg>
    Fill out an application to see if you qualify
  </div>
  <div class="step" style="left:380px">
    <svg width="110" height="110" viewBox="0 0 110 110"><circle cx="55" cy="55" r="52" fill="none" stroke="#fff" stroke-width="3"/><rect x="36" y="32" width="38" height="50" rx="3" fill="none" stroke="#fff" stroke-width="3"/><rect x="46" y="27" width="18" height="9" fill="#4b7aa5" stroke="#fff" stroke-width="3"/><path d="M43 50h24M43 59h24M43 68h16" stroke="#fff" stroke-width="3"/></svg>
    A prescription will be faxed to your primary physician.
  </div>
  <div class="step" style="left:650px">
    <svg width="110" height="110" viewBox="0 0 110 110"><circle cx="55" cy="55" r="52" fill="none" stroke="#fff" stroke-width="3"/><path d="M30 72V56l14-22 8 6-4 8 26 14c6 3 6 10 6 10z" fill="none" stroke="#fff" stroke-width="3" stroke-linejoin="round"/><path d="M30 78h50" stroke="#fff" stroke-width="3"/></svg>
    After the prescription is signed, a certified shoe fitter will fit your new shoes
  </div>
  <div class="step" style="left:920px">
    <svg width="110" height="110" viewBox="0 0 110 110"><circle cx="55" cy="55" r="52" fill="none" stroke="#fff" stroke-width="3"/><path d="M36 56l13 13 26-28" fill="none" stroke="#fff" stroke-width="4" stroke-linecap="round" stroke-linejoin="round"/></svg>
    Enjoy your new shoes!
  </div>
</section>

<section class="abs catalog">
  <h2>REQUEST A FREE DIABETIC SHOE CATALOG</h2>
  <div class="rule"></div>
  <div class="field" style="left:258px;top:112px"><label>First Name:</label><div class="box"></div></div>
  <div class="field" style="left:627px;top:112px"><label>Last Name:</label><div class="box"></div></div>
  <div class="field" style="left:258px;top:164px"><label>Address:</label><div class="box"></div></div>
  <div class="field" style="left:627px;top:164px"><label>City:</label><div class="box"></div></div>
  <div class="field" style="left:258px;top:216px"><label>State:</label><div class="box"></div></div>
  <div class="field" style="left:627px;top:216px"><label>Zip:</label><div class="box"></div></div>
  <div class="field" style="left:258px;top:268px"><label>Phone:</label><div class="box"></div></div>
  <div class="field" style="left:627px;top:268px"><label>Best time to Call:</label><div class="box"></div></div>
  <div class="field" style="left:258px;top:320px"><label>Email:</label><div class="box"></div></div>
  <div class="field" style="left:627px;top:320px"><label>Primary Insurance:</label><div class="box">Elderfund</div></div>
  <div class="field" style="left:258px;top:372px"><label>Do you want to check eligibility Online?</label><div class="box">Yes - Check Eligibility Now</div></div>
  <div class="field" style="left:627px;top:372px"><label>Comments:</label><div class="box tall"></div></div>
  <span class="btn">Request Catalog</span>
</section>

<section class="abs info">
  <div class="info-col" style="left:70px">
    <h3>How Does Diabetes Cause Feet Problems?</h3>
    <p>Diabetes can cause neuropathy (nerve damage), which reduces feeling in your feet. This makes you less likely to feel the early warning signs of foot problems. Decreased circulation reduces the ability to heal and fight off infections. These conditions significantly increase the likelihood of foot complications, infections and ulcers.</p>
  </div>
  <div class="info-col" style="left:445px;width:310px">
    <h3>Why Are Properly Fitted Shoes Important?</h3>
    <p>Twenty-five million people have diabetes, and twenty-five percent of this population will develop foot problems caused by their disease. We provide the most fashionable therapeutic shoes available, in a variety of styles and brands, to help treat and prevent painful diabetic symptoms.</p>
    <p>Our orthopedic shoes reduce the pressure and friction on your feet that can lead to foot injuries. Custom inserts relieve pressure and cushion your feet. Diabetic socks and our therapeutic shoes are also seamless, lined and padded to ensure that there is enough room in the toe box, heel and arch of the shoe. All of these features provide you with the best foot comfort and help prevent potential foot complications.</p>
  </div>
  <div class="info-col" style="left:850px">
    <h3>How Do You Know If Orthopedic Shoes Are Right For You?</h3>
    <p>Anyone with diabetic neuropathy, poor circulation, high risk of infection or nerve damage can benefit from diabetic socks and our shoes. Elderfund patients who qualify are eligible for one pair of shoes and three sets of custom insoles per year at little or no cost to them. Additionally, most private insurance companies will cover the same benefits as Elderfund.</p>
  </div>
</section>

<section class="about">
  <h2 class="abs" style="left:60px;top:1836px">ABOUT US</h2>
  <p class="abs" style="left:60px;top:1896px;width:700px">Pebble Walk Co was created by Harborline Medical Supply to educate clients and prospective shoe fitters about diabetic shoes and the coverage that Elderfund provides. Founded by a Board-Certified Pedorthist, the company's mission is to help clients receive properly fitted shoes from qualified healthcare professionals around the United States. Harborline Medical Supply works directly with Elderfund to determine the patient's coverage.</p>
  <div class="abs photo-block" style="left:824px;top:1839px;width:227px;height:226px" role="img" aria-label="Photo of the company office building with palm trees"></div>
</section>

<div class="abs divider" style="top:2092px"></div>

<section class="philosophy">
  <h2 class="abs" style="left:0;top:2115px">OUR PHILOSOPHY</h2>
  <p class="abs" style="top:2170px">At Harborline Medical Supply, we understand the health benefits and medical safety associated with properly fitted shoes. We strive to educate clients about wearing appropriate footwear and avoiding unnecessary complications. One in four Americans with diabetes will develop potentially serious foot problems related to the disease. By educating our clients and connecting them with leading healthcare professionals, we keep diabetic patients on their feet and mobile. PebbleWalkCo.com further benefits clients by preventing future expenses that result from ill-fitting shoes.</p>
  <p class="abs" style="top:2290px">Harborline Medical Supply connects patients, podiatrists, certified shoe fitters, pedorthists, and providers through its accessible database system. Harborline Medical Supply works with Elderfund directly and helps patients find diabetic shoes and a conveniently located shoe fitter in their area.</p>
  <svg class="abs" style="left:12px;top:2310px" width="14" height="22" viewBox="0 0 14 22"><path d="M11 3L4 11l7 8" fill="none" stroke="#e8a24a" stroke-width="3"/></svg>
</section>

<div class="abs divider" style="top:2374px"></div>

<section class="manufacturers">
  <h2 class="abs" style="left:0;top:2392px">OUR MANUFACTURERS</h2>
  <div class="abs partner" style="left:410px;top:2470px;width:140px;background:#1d3f8a"></div>
  <div class="abs" style="left:610px;top:2497px;width:170px;height:26px;background:#2a2d30;border-radius:3px"></div>
</section>

<div class="abs divider" style="top:2603px"></div>

<p class="abs cta-line" style="top:2636px"><span class="link">CLICK HERE</span> TO VIEW ALL OF OUR <span class="link">WOMEN'S</span> AND <span class="link">MEN'S</span> SHOES</p>
<div class="abs frame" style="left:200px;top:2682px;width:795px;height:138px">
  <div class="fill" role="img" aria-label="Banner photo of men's athletic and leather diabetic shoes" style="background:linear-gradient(90deg,#3d5d86,#2b2b2d 35%,#f1f1f1 50%,#2b2b2d 65%,#7a3b22)"></div>
</div>

<p class="abs cta-line" style="top:2860px"><span class="link">CLICK HERE</span> FOR OUR <span class="link">ELDERFUND</span> PRODUCTS</p>
<div class="abs frame" style="left:157px;top:2900px;width:200px;height:300px"><div class="fill" role="img" aria-label="Photo of a TENS unit with electrode pads" style="background:linear-gradient(180deg,#f4f4f4,#6b6f73,#f4f4f4)"></div></div>
<div class="abs frame" style="left:383px;top:2900px;width:200px;height:300px"><div class="fill" role="img" aria-label="Photo of a lift seat cushion" style="background:radial-gradient(circle at 50% 55%,#2a2c2e 40%,#f4f4f4 70%)"></div></div>
<div class="abs frame" style="left:612px;top:2900px;width:203px;height:300px"><div class="fill" role="img" aria-label="Photo of a blue knee brace" style="background:radial-gradient(circle at 50% 50%,#4a8fc4 25%,#222 45%,#f4f4f4 70%)"></div></div>
<div class="abs frame" style="left:839px;top:2900px;width:202px;height:300px"><div class="fill" role="img" aria-label="Photo of black wrist and ankle braces" style="background:linear-gradient(180deg,#f4f4f4,#1f2123 35%,#1f2123 65%,#f4f4f4)"></div></div>

<footer class="abs site-footer">
  <div class="abs logo" style="left:90px;top:50px"><span class="mark" style="background:#e6e8ea"></span>Pebble Walk Co</div>
  <div class="abs" style="left:90px;top:112px;font-size:19px;display:flex;gap:12px;align-items:center">
    <svg width="18" height="18" viewBox="0 0 24 24"><path d="M6.6 10.8a15 15 0 006.6 6.6l2.2-2.2a1 1 0 011-.25 11.4 11.4 0 003.6.57 1 1 0 011 1V20a1 1 0 01-1 1A17 17 0 013 4a1 1 0 011-1h3.5a1 1 0 011 1 11.4 11.4 0 00.57 3.6 1 1 0 01-.25 1z" fill="#d6d9dc"/></svg>
    1-800-555-0142 &nbsp;Call Us!
  </div>
  <div class="abs" style="left:90px;top:154px;font-size:19px">Follow Us:</div>
  <div class="abs social" style="left:90px;top:193px"></div>
  <div class="abs social" style="left:132px;top:193px"></div>
  <nav class="abs footer-nav">
    Home<br>Pebble Walk Co Do I Qualify?<br>Why Diabetic Shoes?<br>Shoes<br>Products<br>Shoe Fitter Jobs<br>FAQ
  </nav>
  <div class="abs footer-cta">REQUEST A FREE DIABETIC SHOE CATALOG</div>
  <span class="abs btn" style="left:868px;top:150px;width:195px;height:34px;line-height:34px;font-size:17px">Request Catalog</span>
  <svg class="abs" style="left:1122px;top:14px" width="36" height="36" viewBox="0 0 36 36"><circle cx="18" cy="18" r="16" fill="none" stroke="#fff" stroke-width="2"/><path d="M11 21l7-7 7 7" fill="none" stroke="#fff" stroke-width="2.5"/></svg>
  <p class="abs copyright">© PebbleWalkCo.com</p>
</footer>

</body>
</html>
```